Automotive component supplier needs a business card design

We need a business card design for our company called Velmar Global Components Ltd based in the UK. We are a supplier of interior and exterior components to premium car manufacturers such as Corvane Hale, Durrant Fyfe, Maxtorn and Valdessimo. We would like to see a modern business card design that uses the colour blue.

Target Market(s)

Premium automotive car manufacturers.

Industry/Entity Type

Automotive

Contact Information for Business Card

Company Name : Velmar Global Components Limited
Address: 17 Tamsey Yard, Upper Drisk, Warwick, CV31 8RJ, United Kingdom
Web Address : www.velmarparts-example.co.uk

Font styles to use
Other font styles liked:
• Helvetica

Colors
3176b5
0255a3
85acd3
cfdeed
cee9f5
85cae6
34a6d7
0692cd
9bcb3c

Requirements
Must have
• Clear company logo and a mixture of blue colours.
Nice to have
• A high quality modern image.
Should not have
• Multiple colours.

```html
<!DOCTYPE html>
<html lang="en">
<head>
<meta charset="utf-8">
<title>Velmar Global Components – Business Card</title>
<link rel="stylesheet" href="https://fonts.googleapis.com/css2?family=Open+Sans:wght@400;600;700&family=Montserrat:wght@800&display=swap">
<style>
  :root {
    --stage: #0a0b0d;
    --paper: #ffffff;
    --brand-blue: #0b91c8;
    --brand-green: #a6c73f;
    --ink: #1d1d1f;
  }
  * { box-sizing: border-box; margin: 0; padding: 0; }
  html, body { width: 1200px; height: 1200px; overflow: hidden; background: var(--stage); }
  body { position: relative; font-family: "Open Sans", Arial, sans-serif; }

  .card {
    position: absolute;
    left: 181px;
    width: 840px;
    background: var(--paper);
    overflow: hidden;
  }
  .card--front { top: 124px; height: 478px; }
  .card--back { top: 621px; height: 479px; }

  .side-tab {
    position: absolute;
    top: 111px;
    width: 30px;
    height: 256px;
    background: var(--brand-blue);
  }
  .side-tab--left { left: 0; border-radius: 0 22px 22px 0; }
  .side-tab--right { right: 0; border-radius: 22px 0 0 22px; }

  .wordmark {
    position: absolute;
    left: 0; right: 0;
    top: 182px;
    display: flex;
    justify-content: center;
    align-items: center;
    gap: 14px;
  }
  .wordmark__dot {
    width: 18px; height: 18px;
    background: var(--brand-green);
    border-radius: 4px;
    align-self: flex-start;
    margin-top: 8px;
  }
  .wordmark__text {
    font-family: "Montserrat", Arial, sans-serif;
    font-weight: 800;
    color: var(--brand-blue);
    text-align: center;
    line-height: 1;
  }
  .wordmark__name { display: block; font-size: 88px; letter-spacing: 2px; }
  .wordmark__sub { display: block; font-size: 24px; letter-spacing: 1.5px; margin-top: 10px; }

  .identity-panel {
    position: absolute;
    left: 0; top: 0;
    width: 360px; height: 100%;
    background: var(--brand-blue);
    color: var(--paper);
    text-align: center;
  }
  .identity-panel__name {
    position: absolute;
    left: 0; width: 348px;
    top: 212px;
    font-size: 27px;
    font-weight: 400;
    line-height: 1;
  }
  .identity-panel__name strong { font-weight: 700; }
  .identity-panel__role {
    position: absolute;
    left: 0; width: 348px;
    top: 246px;
    font-size: 19px;
    font-weight: 600;
    line-height: 1;
  }
  .accent-tab {
    position: absolute;
    left: 328px; top: 111px;
    width: 32px; height: 256px;
    background: var(--brand-green);
    border-radius: 22px 0 0 22px;
  }

  .contact-list { list-style: none; }
  .contact-item {
    position: absolute;
    left: 388px;
    display: flex;
    align-items: center;
    gap: 8px;
    color: var(--ink);
    font-size: 21.5px;
    line-height: 31px;
  }
  .contact-item__icon { width: 36px; height: 36px; flex: none; }
  .contact-item--address { top: 119px; align-items: flex-start; }
  .contact-item--address .contact-item__icon { margin-top: 8px; }
  .contact-item--phone { top: 194px; }
  .contact-item--mobile { top: 238px; }
  .contact-item--email { top: 282px; }
  .contact-item--web { top: 325px; }
</style>
</head>
<body>

<section class="card card--front" aria-label="Card front">
  <div class="side-tab side-tab--left"></div>
  <div class="side-tab side-tab--right"></div>
  <div class="wordmark">
    <span class="wordmark__text">
      <span class="wordmark__name">VELMAR</span>
      <span class="wordmark__sub">GLOBAL COMPONENTS</span>
    </span>
    <span class="wordmark__dot"></span>
  </div>
</section>

<section class="card card--back" aria-label="Card back">
  <div class="identity-panel">
    <p class="identity-panel__name">LORIN <strong>ASHCOMBE</strong></p>
    <p class="identity-panel__role">GRAPHIX DESIGNER</p>
  </div>
  <div class="accent-tab"></div>

  <ul class="contact-list">
    <li class="contact-item contact-item--address">
      <svg class="contact-item__icon" viewBox="0 0 36 36" aria-hidden="true">
        <circle cx="18" cy="18" r="16.5" fill="none" stroke="#a6c73f" stroke-width="2"/>
        <path d="M18 8c-4 0-7 3-7 7 0 5 7 13 7 13s7-8 7-13c0-4-3-7-7-7z" fill="#a6c73f"/>
        <circle cx="18" cy="15" r="2.6" fill="#fff"/>
      </svg>
      <span>17 Tamsey Yard, Upper Drisk,<br>Warwick, CV31 8RJ, United Kingdom.</span>
    </li>
    <li class="contact-item contact-item--phone">
      <svg class="contact-item__icon" viewBox="0 0 36 36" aria-hidden="true">
        <circle cx="18" cy="18" r="16.5" fill="none" stroke="#a6c73f" stroke-width="2"/>
        <path d="M9 15c0-3 4-4 9-4s9 1 9 4v2h-5v-2h-8v2H9z" fill="#a6c73f"/>
        <path d="M12 18h12l2 8H10z" fill="#a6c73f"/>
        <circle cx="18" cy="22" r="2.2" fill="#fff"/>
      </svg>
      <span>000. 123. 4567</span>
    </li>
    <li class="contact-item contact-item--mobile">
      <svg class="contact-item__icon" viewBox="0 0 36 36" aria-hidden="true">
        <circle cx="18" cy="18" r="16.5" fill="none" stroke="#a6c73f" stroke-width="2"/>
        <path d="M12 9l4 0 1 5-2.5 2c1 2.5 3 4.5 5.5 5.5l2-2.5 5 1v4c0 1-1 2-2 2C16 26 10 20 10 11c0-1 1-2 2-2z" fill="#a6c73f"/>
      </svg>
      <span>000. 123. 4567</span>
    </li>
    <li class="contact-item contact-item--email">
      <svg class="contact-item__icon" viewBox="0 0 36 36" aria-hidden="true">
        <circle cx="18" cy="18" r="16.5" fill="none" stroke="#a6c73f" stroke-width="2"/>
        <rect x="10" y="12" width="16" height="12" rx="1.5" fill="#a6c73f"/>
        <path d="M10.5 13l7.5 6 7.5-6" fill="none" stroke="#fff" stroke-width="1.6"/>
      </svg>
      <span>hello@velmarmail-example.co.uk</span>
    </li>
    <li class="contact-item contact-item--web">
      <svg class="contact-item__icon" viewBox="0 0 36 36" aria-hidden="true">
        <circle cx="18" cy="18" r="16.5" fill="none" stroke="#a6c73f" stroke-width="2"/>
        <circle cx="18" cy="18" r="10" fill="none" stroke="#a6c73f" stroke-width="2"/>
        <ellipse cx="18" cy="18" rx="4.5" ry="10" fill="none" stroke="#a6c73f" stroke-width="1.6"/>
        <path d="M8 18h20M10 13h16M10 23h16" stroke="#a6c73f" stroke-width="1.6"/>
      </svg>
      <span>www.velmarparts-example.co.uk</span>
    </li>
  </ul>
</section>

</body>
</html>
```